one pager for investors

I will give an initial file in any format needed. Also, the photo that must be included. As well as the logo, that must be the key to the overall design in terms of font, colors, and general layout. I will attach a file in PDF format, which is a one pager presenting a project for investors that I would like to attract and convinced to invest in my project. What I would like you to do is propose me different and better design options, taking my first draft as an example. But you must absolutely keep every single word and number, absolutely all the information written in my first draft(except “ TEMPLATE DRAFT”). Also, on the top left corner is the logo of our company, which I think should be your main inspiration document is a one pager presented to potential investors that not only has to include the most important information in order for them to be able to see everything needed to see the value of the project (which I’ve already taken care of by writing the text needed, numbers presented and timeline shown; all of which which must be preserved in terms of content, but can be completely redesigned and manipulated ) sh a.k.a. Project summary for investor to go for it.
Target Market(s)
Serious rich investors
Industry/Entity Type
Real eatate

```html
<!DOCTYPE html>
<html lang="fr">
<head>
<meta charset="utf-8">
<title>Description du projet – Valmont Properties SA</title>
<link href="https://fonts.googleapis.com/css2?family=Inter:wght@300;400;600;700&display=swap" rel="stylesheet">
<style>
  :root {
    --ink: #1e1e1e;
    --panel: #f0f0f1;
    --frame: #3a3a3a;
    --sky-top: #dfe5ee;
    --sky-mid: #cfd6df;
    --paper: #ffffff;
  }
  * { box-sizing: border-box; margin: 0; padding: 0; }
  html, body { width: 848px; height: 1200px; overflow: hidden; background: var(--paper); }
  body { font-family: "Inter", Arial, sans-serif; color: var(--ink); }

  .sheet { position: relative; width: 848px; height: 1200px; border: 1px solid var(--ink); overflow: hidden; }

  .hero-visual {
    position: absolute; left: 0; top: 0; width: 848px; height: 560px;
    background:
      linear-gradient(to bottom, rgba(255,255,255,0) 70%, var(--paper) 100%),
      linear-gradient(to right, rgba(126,138,106,0.55) 0%, rgba(126,138,106,0) 22%, rgba(126,138,106,0) 78%, rgba(181,118,90,0.45) 100%),
      linear-gradient(to bottom, #ffffff 0%, var(--sky-top) 18%, var(--sky-mid) 45%, #c4b3a5 70%, #b9bfa8 88%);
  }

  .brand { position: absolute; left: 0; top: 82px; width: 100%; text-align: center; font-weight: 600; font-size: 30px; letter-spacing: 4px; line-height: 1; color: var(--ink); }

  .confidential { position: absolute; top: 543px; left: 0; width: 100%; text-align: center; font-size: 16px; }
  .title-band { position: absolute; left: 61px; width: 726px; top: 572px; height: 41px; border-top: 1px solid var(--ink); border-bottom: 1px solid var(--ink); text-align: center; }
  .title-band h1 { font-weight: 300; font-size: 33px; line-height: 40px; letter-spacing: 0.3px; }

  .summary { position: absolute; left: 61px; width: 726px; top: 621px; font-size: 13.4px; line-height: 17px; text-align: justify; text-align-last: center; font-weight: 300; }
  .duration { position: absolute; top: 682px; left: 0; width: 100%; text-align: center; font-weight: 700; font-size: 16px; }

  .panel { position: absolute; top: 723px; width: 347px; height: 300px; }
  .panel.finance { left: 59px; }
  .panel.invest { left: 441px; }
  .panel-frame { position: absolute; left: 0; top: 0; }
  .panel h2 { position: absolute; top: 26px; height: 21px; border-top: 1px solid var(--frame); border-bottom: 1px solid var(--frame); font-size: 16px; font-weight: 700; text-align: center; line-height: 20px; letter-spacing: 0.3px; }
  .finance h2 { left: 40px; width: 265px; }
  .invest h2 { left: 22px; width: 302px; }

  .row { position: absolute; font-size: 13.5px; font-weight: 300; line-height: 16px; white-space: nowrap; }
  .row .label { position: absolute; left: 0; }
  .row .value { position: absolute; }
  .finance .row { left: 40px; }
  .finance .row .value { left: 161px; }
  .invest .row { left: 22px; }
  .invest .row .value { left: 202px; }
  .row.strong { font-weight: 700; }

  .timeline { position: absolute; left: 0; top: 1040px; width: 848px; height: 80px; }
  .timeline svg { position: absolute; left: 0; top: 0; }
  .tl-date, .tl-label { position: absolute; transform: translateX(-50%); white-space: nowrap; font-size: 13.5px; }
  .tl-date { top: 11px; font-weight: 700; }
  .tl-label { top: 55px; font-weight: 300; }

  .footer { position: absolute; top: 1135px; left: 0; width: 100%; text-align: center; font-size: 13.5px; font-weight: 300; }
</style>
</head>
<body>
<main class="sheet">
  <div class="hero-visual" role="img" aria-label="Rendu architectural d'un immeuble résidentiel moderne à balcons vitrés entouré de jardins et d'arbres"></div>

  <header class="brand">VALMONT PROPERTIES SA</header>

  <p class="confidential">CONFIDENTIEL – Projet imobilier “XXX”</p>
  <div class="title-band"><h1>DESCRIPTION DU PROJET</h1></div>

  <p class="summary">Le projet XXX est un projet de dévloppement de 30 appartements de standing en PPE au centre de Lausanne. Le terrain a été sécurisé par la signature du vente à terme conditionnelle. L’objectif est d’obtenir le permis de construire, puis de ventre les lots. Dans un premier temps sur plan puis au fil de la construction.</p>
  <p class="duration">Durée estimée du projet – 24 à 36 mois.</p>

  <section class="panel finance">
    <svg class="panel-frame" width="347" height="300" viewBox="0 0 347 300" aria-hidden="true">
      <path d="M12.5 0.5 H334.5 V12.5 H346.5 V287.5 H334.5 V299.5 H12.5 V287.5 H0.5 V12.5 H12.5 Z" fill="#f0f0f1" stroke="#3a3a3a" stroke-width="1"/>
      <path d="M16.5 4.5 H330.5 V16.5 H342.5 V283.5 H330.5 V295.5 H16.5 V283.5 H4.5 V16.5 H16.5 Z" fill="none" stroke="#3a3a3a" stroke-width="1"/>
    </svg>
    <h2>PLAN FINANCIER</h2>
    <div class="row" style="top:60px"><span class="label">Prix du terrain</span><span class="value">CHF 2’000’000</span></div>
    <div class="row" style="top:78px"><span class="label">Frais d’acquisition</span><span class="value">CHF 100’000</span></div>
    <div class="row" style="top:97px"><span class="label">Coût de construction</span><span class="value">CHF 2’500’000</span></div>
    <div class="row" style="top:115px"><span class="label">Divers &amp; imprévus</span><span class="value">CHF 200’000</span></div>
    <div class="row strong" style="top:134px"><span class="label">Prix de revient total</span><span class="value">CHF 4’800’000</span></div>
    <div class="row strong" style="top:175px"><span class="label">Prix de vente total</span><span class="value">CHF 7’500’000</span></div>
    <div class="row" style="top:198px"><span class="label">Honoraires sur vente</span><span class="value">CHF 190’000</span></div>
    <div class="row strong" style="top:234px"><span class="label">Marge projet</span><span class="value">CHF 2’510’000</span></div>
    <div class="row strong" style="top:257px"><span class="label">En % sur prix de vente</span><span class="value">33.47%</span></div>
  </section>

  <section class="panel invest">
    <svg class="panel-frame" width="347" height="300" viewBox="0 0 347 300" aria-hidden="true">
      <path d="M12.5 0.5 H334.5 V12.5 H346.5 V287.5 H334.5 V299.5 H12.5 V287.5 H0.5 V12.5 H12.5 Z" fill="#f0f0f1" stroke="#3a3a3a" stroke-width="1"/>
      <path d="M16.5 4.5 H330.5 V16.5 H342.5 V283.5 H330.5 V295.5 H16.5 V283.5 H4.5 V16.5 H16.5 Z" fill="none" stroke="#3a3a3a" stroke-width="1"/>
    </svg>
    <h2>STRUCTURE D’INVESTISSEMENT</h2>
    <div class="row" style="top:60px"><span class="label">Besoin de fonds propres</span><span class="value">CHF 2’000’000</span></div>
    <div class="row" style="top:78px"><span class="label">Retour de fonds total</span><span class="value">CHF 3’156’600</span></div>
    <div class="row strong" style="top:115px"><span class="label">Bénéfice net investisseur</span><span class="value">CHF 1’656’600</span></div>
    <div class="row" style="top:134px"><span class="label">Soit 2/3 du bénéfice projet</span></div>
    <div class="row strong" style="top:175px"><span class="label">Multiads propres</span><span class="value">x1.83</span></div>
    <div class="row strong" style="top:216px"><span class="label">Rendement annualisé</span><span class="value">41.4%</span></div>
    <div class="row" style="top:234px"><span class="label">Calcul sur 24 mois</span></div>
  </section>

  <section class="timeline">
    <svg width="848" height="80" viewBox="0 0 848 80" aria-hidden="true">
      <line x1="90" y1="40" x2="752" y2="40" stroke="#1e1e1e" stroke-width="2.5"/>
      <polygon points="749,31 760,40 749,49" fill="#1e1e1e"/>
      <line x1="148" y1="30" x2="148" y2="50" stroke="#1e1e1e" stroke-width="1.5"/>
      <line x1="317" y1="30" x2="317" y2="50" stroke="#1e1e1e" stroke-width="1.5"/>
      <line x1="524" y1="30" x2="524" y2="50" stroke="#1e1e1e" stroke-width="1.5"/>
      <line x1="715" y1="30" x2="715" y2="50" stroke="#1e1e1e" stroke-width="1.5"/>
    </svg>
    <span class="tl-date" style="left:148px">08.2024</span>
    <span class="tl-date" style="left:317px">04.2025</span>
    <span class="tl-date" style="left:524px">12.2025</span>
    <span class="tl-date" style="left:715px">12.2025</span>
    <span class="tl-label" style="left:148px">Achat parcelle</span>
    <span class="tl-label" style="left:317px">Mise à l’enquête</span>
    <span class="tl-label" style="left:524px">Début construction</span>
    <span class="tl-label" style="left:715px">12.2025</span>
  </section>

  <footer class="footer">Valmont Properties Vaud SA - Rue des Tilleuls 8 - CH-1110 Morges</footer>
</main>
</body>
</html>
```